Ridgewell Stonecraft Construction Needs business card

Hey we are in need of business card designs. I have upload our logo as a guideline, but free feel to run with it or come up with something unique.
Pls have fun with it and be creative. the name says it all!
i will give some directions after i see a few entries..
Logo source file has been uploaded..
Hey because of the logo is so colourful already.
Can we have a few submissions with less colour.
Also we are looking for clever/hidden/descriptive business card.

```html
<!DOCTYPE html>
<html lang="en">
<head>
<meta charset="utf-8">
<title>Ridgewell Stonecraft Construction – Business Card</title>
<link rel="stylesheet" href="https://fonts.googleapis.com/css2?family=Arimo:wght@400;700&display=swap">
<style>
  :root {
    --stage: #e6e3df;
    --card-white: #ffffff;
    --slate: #5b6263;
    --slate-text: #f2f3f3;
    --brand-grey: #5a5f61;
    --accent-blue: #5aa9e6;
  }
  * { margin: 0; padding: 0; box-sizing: border-box; }
  html, body {
    width: 1200px; height: 470px; overflow: hidden;
    background: var(--stage);
    font-family: "Arimo", Arial, sans-serif;
  }
  .stage { position: relative; width: 1200px; height: 470px; }
  .card {
    position: absolute; top: 70px;
    width: 560px; height: 330px;
    background: var(--card-white);
    box-shadow: 0 4px 14px rgba(0,0,0,0.18);
    overflow: hidden;
  }
  .card--info { left: 25px; }
  .card--front { left: 615px; }

  .card__brand-side {
    position: absolute; left: 0; top: 0; width: 268px; height: 100%;
    display: flex; align-items: center; justify-content: center;
  }
  .brand {
    color: var(--brand-grey); font-weight: 700; text-align: center;
    letter-spacing: 0.5px; line-height: 1.1;
  }
  .brand__square {
    display: block; margin: 0 auto 12px;
    width: 14px; height: 14px; background: var(--accent-blue);
  }
  .brand--small .brand__name { font-size: 23px; }
  .brand--small .brand__tag { font-size: 11px; letter-spacing: 2px; margin-top: 4px; }
  .brand--large .brand__square { width: 22px; height: 22px; margin-bottom: 20px; }
  .brand--large .brand__name { font-size: 40px; }
  .brand--large .brand__tag { font-size: 17px; letter-spacing: 3px; margin-top: 8px; }

  .card__contact-side {
    position: absolute; left: 268px; top: 0; right: 0; height: 100%;
    background: var(--slate); color: var(--slate-text);
    padding: 82px 24px 0 26px;
  }
  .person__name { font-size: 17px; }
  .person__title { font-size: 12px; margin-top: 3px; }
  .contact-list { list-style: none; margin-top: 30px; font-size: 13px; }
  .contact-list li { display: flex; align-items: center; gap: 6px; margin-bottom: 4px; }
  .contact-list svg { width: 12px; height: 12px; flex: none; }
  .address { margin-top: 34px; font-size: 13px; line-height: 1.35; }

  .card--front .card__centre {
    position: absolute; inset: 0;
    display: flex; align-items: center; justify-content: center;
  }
</style>
</head>
<body>
<main class="stage">
  <section class="card card--info" aria-label="Business card, contact side">
    <div class="card__brand-side">
      <div class="brand brand--small">
        <span class="brand__square"></span>
        <div class="brand__name">RIDGEWELL STONECRAFT</div>
        <div class="brand__tag">CONSTRUCTION</div>
      </div>
    </div>
    <div class="card__contact-side">
      <div class="person__name">Your Name</div>
      <div class="person__title">Title</div>
      <ul class="contact-list">
        <li><svg viewBox="0 0 12 12" aria-hidden="true"><circle cx="6" cy="6" r="5.3" fill="none" stroke="currentColor" stroke-width="1"/><path d="M4 3.2l1.2 1.6-.7.8c.5 1 1.1 1.6 2 2l.8-.7 1.6 1.2-.8 1c-2.4-.4-4.5-2.5-4.9-4.9z" fill="currentColor"/></svg>0491 570 156</li>
        <li><svg viewBox="0 0 12 12" aria-hidden="true"><circle cx="6" cy="6" r="5.3" fill="none" stroke="currentColor" stroke-width="1"/><path d="M4 3.2l1.2 1.6-.7.8c.5 1 1.1 1.6 2 2l.8-.7 1.6 1.2-.8 1c-2.4-.4-4.5-2.5-4.9-4.9z" fill="currentColor"/></svg>0491 570 156</li>
        <li><svg viewBox="0 0 12 12" aria-hidden="true"><circle cx="6" cy="6" r="6" fill="currentColor"/><rect x="3" y="4" width="6" height="4.2" fill="var(--slate)"/><path d="M3 4l3 2.3L9 4" fill="none" stroke="currentColor" stroke-width="0.8"/></svg>hello@ridgewellstone.com</li>
        <li><svg viewBox="0 0 12 12" aria-hidden="true"><circle cx="6" cy="6" r="5.3" fill="none" stroke="currentColor" stroke-width="1"/><ellipse cx="6" cy="6" rx="2.3" ry="5.3" fill="none" stroke="currentColor" stroke-width="0.8"/><path d="M0.8 6h10.4M1.8 3.5h8.4M1.8 8.5h8.4" stroke="currentColor" stroke-width="0.7"/></svg>www.ridgewellstone.com</li>
      </ul>
      <div class="address">Street Name City Name<br>State Zipcode</div>
    </div>
  </section>

  <section class="card card--front" aria-label="Business card, front">
    <div class="card__centre">
      <div class="brand brand--large">
        <span class="brand__square"></span>
        <div class="brand__name">RIDGEWELL STONECRAFT</div>
        <div class="brand__tag">CONSTRUCTION</div>
      </div>
    </div>
  </section>
</main>
</body>
</html>
```